don't add new designs, a winner will be choosed A website for mothers about homeopathy

We have a blog www.lottamaus.eu based on WordPress (Wix would be also good) about homeopathy-critique and health issues.
Our logo is a little girl Henrike, the background color green.
It looks somehow good, but we want to be up to date:).
Our goal is to open eyes from propaganda and misinformation on the web. We are all volunteers and invest our time and money for this purpose. Once people like it, we are happy to translate our blog to the English.
Updates

Please, don't submit a new design. we will choose from the designs we already have. Thank you! Added Thursday, July 20, 2017

Target Market(s)

mothers, people reading about health

Industry/Entity Type

Health

Number of Pages Required

3 page

Colors
abd037

Requirements
Must have
• - nice, friendly, evoking positive emotions
• - colorful (see for example how it looks now)
• - a good way how to show up articles (actually, if you open an article, you have to scroll, it appears on the bottom of the page)
• - We need to arrange stuff, where to put "most read", "Category", "contact", "themes" "search" (now, everything is on the right side. if you like it so, ok)
Nice to have
• Everything is in German, but I am happy to translate everything you need.
• The big text is: Lottchen mag keine Kügelchen: Henrike wants no Pellets (the sugar pills of homeopathy)
• "(Nicht nur) homöopathiekritische Informationen für Eltern und alle, die für unsere Kleinen sorgen" - (Not only) Homeopathy-critique Information for Parents and All Who Take Care Of Our Small (Children)
• - there are many of the pictures of Henrike, you can choose the best one. You can find them here https://www.verbund-faktenblick.eu/lottchen-mag-keine-kuegelchen
• - we have also a FB, which could be integrated https://www.facebook.com/lottchenmagkeinekuegelchen/?fref=ts
Should not have
• - a sterile modern look

```html
<!DOCTYPE html>
<html lang="en">
<head>
<meta charset="utf-8">
<title>Lottamaus – Blog</title>
<link href="https://fonts.googleapis.com/css2?family=Roboto:wght@400;500;700;900&family=Roboto+Condensed:wght@700&display=swap" rel="stylesheet">
<style>
:root{
  --green:#9cc83b;
  --green-dark:#7aa82a;
  --green-deep:#2f6b2a;
  --ink:#222;
  --text:#666;
  --muted:#999;
  --line:#e6e6e6;
  --page:#f4f4f4;
  --card:#fff;
  --footer:#161616;
}
*{box-sizing:border-box;margin:0;padding:0}
html,body{width:1200px;height:3836px;overflow:hidden}
body{font-family:"Roboto",Arial,sans-serif;color:var(--text);background:var(--page);position:relative}

/* header */
.site-header{height:140px;background:#fff;position:relative}
.brand{position:absolute;left:28px;top:26px;display:flex;align-items:center;gap:12px}
.brand-dot{width:52px;height:52px;border-radius:50%;background:var(--green)}
.brand-name{font-size:20px;font-weight:700;color:var(--green-deep)}
.contact-bar{position:absolute;right:30px;top:18px;display:flex;align-items:center;gap:34px}
.phone{display:flex;align-items:center;gap:10px;font-weight:700;color:var(--ink);font-size:17px}
.phone-icon{width:34px;height:34px;border-radius:50%;background:var(--green);display:flex;align-items:center;justify-content:center}
.partner{display:flex;align-items:center;gap:8px;font-weight:700;color:var(--green-deep);font-size:18px}
.partner-square{width:26px;height:26px;background:var(--green-deep)}
.main-nav{position:absolute;right:30px;top:94px;display:flex;gap:30px}
.main-nav a{font-size:13px;font-weight:700;color:var(--ink);text-decoration:none;letter-spacing:.3px}

/* hero */
.hero{height:612px;position:relative;overflow:hidden}
.hero-art{position:absolute;inset:0;background:linear-gradient(180deg,#cfe7a7 0%,#9fcf5d 40%,#5f9a35 75%,#4c7f2c 100%)}
.hero-title{position:absolute;left:0;right:0;top:360px;text-align:center;font-family:"Roboto Condensed",sans-serif;font-size:68px;color:#fff;letter-spacing:3px;padding-left:120px}
.hero-arrow{position:absolute;top:430px;width:40px;height:40px;border-radius:50%;background:rgba(255,255,255,.85);display:flex;align-items:center;justify-content:center}
.hero-arrow.prev{left:20px}.hero-arrow.next{right:20px}

/* layout */
.content{position:absolute;left:152px;top:848px;width:956px;display:flex;gap:32px}
.posts{width:568px;display:flex;flex-direction:column;gap:32px}
.sidebar{width:356px;display:flex;flex-direction:column;gap:28px}

/* post card */
.post{background:var(--card);height:460px;box-shadow:0 2px 8px rgba(0,0,0,.12);position:relative}
.post-media{height:222px;position:relative}
.post-date{position:absolute;left:0;top:12px;display:flex;align-items:center;gap:8px;background:rgba(0,0,0,.45);color:#fff;font-size:12px;padding:4px 14px 4px 8px}
.post-date i{width:20px;height:20px;border-radius:50%;background:var(--green);display:block}
.post-body{padding:18px 20px 0}
.post-title{font-family:"Roboto Condensed",sans-serif;font-size:17px;color:var(--ink);text-transform:uppercase;line-height:1.3;margin-bottom:12px}
.post-excerpt{font-size:12.5px;line-height:1.65;color:var(--muted)}
.read-more{display:block;text-align:right;font-size:11px;font-weight:700;color:var(--ink);margin-top:10px}
.post-meta{position:absolute;left:0;right:0;bottom:0;height:60px;border-top:1px solid var(--line);display:flex;align-items:center;padding:0 20px;gap:28px;font-size:12px;color:var(--muted)}
.post-meta span{display:flex;align-items:center;gap:6px}
.post-meta b{width:10px;height:10px;border-radius:50%;background:var(--green);display:block}
.post-fab{position:absolute;right:18px;bottom:12px;width:36px;height:36px;border-radius:50%;background:var(--green-deep);display:flex;align-items:center;justify-content:center}

/* pagination */
.pagination{position:absolute;left:152px;width:568px;top:3312px;display:flex;justify-content:center;gap:10px}
.pagination span{width:34px;height:34px;border-radius:50%;border:1px solid #ccc;background:#fff;display:flex;align-items:center;justify-content:center;font-size:13px;color:var(--ink)}
.pagination .on,.pagination .arrow{background:var(--green);border-color:var(--green);color:#fff}

/* widgets */
.widget{background:var(--card);box-shadow:0 2px 8px rgba(0,0,0,.1)}
.widget-head{background:var(--green);color:#fff;font-size:13px;font-weight:700;text-transform:uppercase;padding:10px 14px;letter-spacing:.4px;display:flex;justify-content:space-between}
.widget-body{padding:14px;font-size:12px;line-height:1.6}
.about{display:flex;gap:12px}
.about-pic{width:64px;height:64px;flex:none;background:linear-gradient(#f7d774,#9cc83b)}
.about strong{display:block;color:var(--ink);font-size:12px}
.widget a{color:var(--green-deep);text-decoration:none}
.archive li{list-style:none;font-weight:700;color:var(--ink);margin:4px 0}
.archive ul ul{margin-left:16px}
.archive ul ul ul li{font-weight:400;color:var(--green-deep)}
.news-item{display:flex;gap:12px;margin-bottom:12px}
.news-thumb{width:84px;height:54px;flex:none}
.news-item strong{display:block;color:var(--ink);font-size:12px}
.news-item small{color:var(--muted);font-size:11px}
.field{border:1px solid #ddd;height:34px;margin-top:10px;padding:8px;color:#aaa;font-size:12px}
.btn{display:inline-block;margin-top:12px;background:var(--green-deep);color:#fff;font-size:12px;font-weight:700;padding:8px 18px}
.fb-cover{height:120px;background:linear-gradient(135deg,#f5d46a,#88b7d9)}
.fb-friends{display:flex;gap:6px;margin-top:8px}
.fb-friends i{width:40px;height:40px;display:block;background:#c9d6c0}
.testimonial{text-align:center;padding:22px 20px}
.avatar{width:84px;height:84px;border-radius:50%;margin:0 auto 10px;background:linear-gradient(#e8c4a8,#a8695a)}
.testimonial strong{color:var(--ink);font-size:13px;display:block}
.dots{display:flex;justify-content:center;gap:6px;margin-top:12px}
.dots i{width:8px;height:8px;border-radius:50%;background:#ccc;display:block}
.dots i.on{background:var(--green)}

/* footer */
.site-footer{position:absolute;left:0;right:0;top:3420px;height:416px;color:#ccc;text-align:center}
.footer-curve{position:absolute;left:0;top:0}
.footer-inner{position:absolute;left:0;right:0;top:120px}
.socials{display:flex;justify-content:center;gap:16px}
.socials i{width:40px;height:40px;border-radius:50%;border:1px solid #777;display:block}
.footer-nav{display:flex;justify-content:center;gap:90px;margin-top:32px;font-size:13px;color:#fff;font-weight:500}
.footer-nav.sub{gap:60px;margin-top:18px;font-size:12px;color:#bbb;font-weight:400}
.footer-rule{width:900px;height:1px;background:#333;margin:34px auto 24px}
.copyright{font-size:11px;color:#888}
</style>
</head>
<body>

<header class="site-header">
  <div class="brand"><span class="brand-dot"></span><span class="brand-name">Lottamaus</span></div>
  <div class="contact-bar">
    <div class="phone"><span class="phone-icon"><svg width="16" height="16" viewBox="0 0 24 24"><path fill="#fff" d="M6.6 10.8a15 15 0 0 0 6.6 6.6l2.2-2.2a1 1 0 0 1 1-.25 11.4 11.4 0 0 0 3.6.6 1 1 0 0 1 1 1V20a1 1 0 0 1-1 1A17 17 0 0 1 3 4a1 1 0 0 1 1-1h3.5a1 1 0 0 1 1 1c0 1.25.2 2.45.6 3.6a1 1 0 0 1-.25 1z"/></svg></span>+49 151 2345 6789</div>
    <div class="partner"><span class="partner-square"></span>Faktenblick</div>
  </div>
  <nav class="main-nav"><a>HOME</a><a>ARTICLES AND LINKS</a><a>ABOUT THE HENRIKE</a><a>HENRIKE'S SHOP</a><a>CONTACT US</a></nav>
</header>

<section class="hero">
  <div class="hero-art" role="img" aria-label="Illustration of the little girl Henrike and her dog in a sunny green forest"></div>
  <h1 class="hero-title">LOTTCHEN</h1>
  <span class="hero-arrow prev"><svg width="14" height="14" viewBox="0 0 14 14"><path d="M9 2 4 7l5 5" stroke="#555" stroke-width="2" fill="none"/></svg></span>
  <span class="hero-arrow next"><svg width="14" height="14" viewBox="0 0 14 14"><path d="m5 2 5 5-5 5" stroke="#555" stroke-width="2" fill="none"/></svg></span>
</section>

<main class="content">
  <div class="posts">
    <article class="post">
      <div class="post-media" role="img" aria-label="Photo of a baby being given a small pill" style="background:linear-gradient(135deg,#e9b9b4,#c97f86)"><span class="post-date"><i></i>Published On 21 July 2017</span></div>
      <div class="post-body"><h2 class="post-title">My opinion on homeopathy? Perhaps you would like facts?</h2>
      <p class="post-excerpt">The sugar pills promise gentle help without side effects, but the evidence tells a different story. Here we look calmly at what studies really show and why parents deserve clear facts.</p>
      <span class="read-more">READ MORE</span></div>
      <div class="post-meta"><span><b></b>Jonas Weber</span><span><b></b>9 Comments</span><span><b></b>1,523 Views</span><span><b></b>10 Favourites</span></div>
      <span class="post-fab"><svg width="14" height="14" viewBox="0 0 14 14"><path d="M2 10 9 3l2 2-7 7H2z" fill="#fff"/></svg></span>
    </article>
    <article class="post">
      <div class="post-media" role="img" aria-label="Photo of a bright waiting room in a doctor's practice" style="background:linear-gradient(135deg,#eef0ee,#b9c2bd)"><span class="post-date"><i></i>Published On 21 July 2017</span></div>
      <div class="post-body"><h2 class="post-title">Selbstmedikation mit Homöopathie – klar!, oder doch...</h2>
      <p class="post-excerpt">The sugar pills promise gentle help without side effects, but the evidence tells a different story. Here we look calmly at what studies really show and why parents deserve clear facts.</p>
      <span class="read-more">READ MORE</span></div>
      <div class="post-meta"><span><b></b>Jonas Weber</span><span><b></b>9 Comments</span><span><b></b>1,523 Views</span><span><b></b>10 Favourites</span></div>
      <span class="post-fab"><svg width="14" height="14" viewBox="0 0 14 14"><path d="M2 10 9 3l2 2-7 7H2z" fill="#fff"/></svg></span>
    </article>
    <article class="post">
      <div class="post-media" role="img" aria-label="Illustration of Henrike standing in a blossoming spring garden" style="background:linear-gradient(135deg,#cfe3a6,#6e9c3e)"><span class="post-date"><i></i>Published On 21 July 2017</span></div>
      <div class="post-body"><h2 class="post-title">Ein paar Gedanken zur „Anthroposophischen Medizin“</h2>
      <p class="post-excerpt">The sugar pills promise gentle help without side effects, but the evidence tells a different story. Here we look calmly at what studies really show and why parents deserve clear facts.</p>
      <span class="read-more">READ MORE</span></div>
      <div class="post-meta"><span><b></b>Jonas Weber</span><span><b></b>9 Comments</span><span><b></b>1,523 Views</span><span><b></b>10 Favourites</span></div>
      <span class="post-fab"><svg width="14" height="14" viewBox="0 0 14 14"><path d="M2 10 9 3l2 2-7 7H2z" fill="#fff"/></svg></span>
    </article>
    <article class="post">
      <div class="post-media" role="img" aria-label="Photo of rows of amber glass jars on shelves" style="background:linear-gradient(135deg,#d9822b,#7a3a12)"><span class="post-date"><i></i>Published On 21 July 2017</span></div>
      <div class="post-body"><h2 class="post-title">Der Kinderdoc zur Reisekrankheit</h2>
      <p class="post-excerpt">The sugar pills promise gentle help without side effects, but the evidence tells a different story. Here we look calmly at what studies really show and why parents deserve clear facts.</p>
      <span class="read-more">READ MORE</span></div>
      <div class="post-meta"><span><b></b>Jonas Weber</span><span><b></b>9 Comments</span><span><b></b>1,523 Views</span><span><b></b>10 Favourites</span></div>
      <span class="post-fab"><svg width="14" height="14" viewBox="0 0 14 14"><path d="M2 10 9 3l2 2-7 7H2z" fill="#fff"/></svg></span>
    </article>
    <article class="post">
      <div class="post-media" role="img" aria-label="Photo of a sleeping newborn baby" style="background:linear-gradient(135deg,#f1ddd0,#c9a28c)"><span class="post-date"><i></i>Published On 21 July 2017</span></div>
      <div class="post-body"><h2 class="post-title">Thema: Placebo – heute: Placebo ist nicht Einbildung!</h2>
      <p class="post-excerpt">The sugar pills promise gentle help without side effects, but the evidence tells a different story. Here we look calmly at what studies really show and why parents deserve clear facts.</p>
      <span class="read-more">READ MORE</span></div>
      <div class="post-meta"><span><b></b>Jonas Weber</span><span><b></b>9 Comments</span><span><b></b>1,523 Views</span><span><b></b>10 Favourites</span></div>
      <span class="post-fab"><svg width="14" height="14" viewBox="0 0 14 14"><path d="M2 10 9 3l2 2-7 7H2z" fill="#fff"/></svg></span>
    </article>
  </div>

  <aside class="sidebar">
    <section class="widget">
      <h3 class="widget-head">About Me</h3>
      <div class="widget-body">
        <div class="about"><div class="about-pic" role="img" aria-label="Small illustration of Henrike"></div>
        <div><strong>HENRIKE</strong>Henrike is a curious little girl who wants no pellets, only honest answers about health.</div></div>
        <p style="margin-top:8px"><a>View my complete profile</a></p>
      </div>
    </section>
    <section class="widget archive">
      <h3 class="widget-head">Blog Archive</h3>
      <div class="widget-body"><ul>
        <li>▾ 2017 (7)<ul><li>▾ July (4)<ul><li>View my complete profile</li><li>Gentle facts for parents</li><li>Why pellets are sugar</li><li>Notes on travel sickness</li></ul></li></ul></li>
        <li>▸ 2016 (7)</li><li>▸ 2015 (7)</li></ul></div>
    </section>
    <section class="widget">
      <h3 class="widget-head">Recent News</h3>
      <div class="widget-body">
        <div class="news-item"><div class="news-thumb" role="img" aria-label="Thumbnail of a child with a dog" style="background:#b8915c"></div><div><strong>LOREM IPSUM IS NOT SIMPLY</strong><small>20 Apr 2017 Henrike</small></div></div>
        <div class="news-item"><div class="news-thumb" role="img" aria-label="Thumbnail of a family outdoors" style="background:#7fa6c8"></div><div><strong>LOREM IPSUM IS NOT SIMPLY</strong><small>20 Apr 2017 Henrike</small></div></div>
        <div class="news-item"><div class="news-thumb" role="img" aria-label="Thumbnail of a classroom" style="background:#c9b8a0"></div><div><strong>LOREM IPSUM IS NOT SIMPLY</strong><small>20 Apr 2017 Henrike</small></div></div>
      </div>
    </section>
    <section class="widget">
      <h3 class="widget-head">Subscribe to our mail</h3>
      <div class="widget-body">
        <p>Enter your email to receive new articles directly in your inbox.</p>
        <div class="field">Name</div><div class="field">Enter email</div>
        <span class="btn">SUBSCRIBE</span>
      </div>
    </section>
    <section class="widget">
      <h3 class="widget-head">Facebook Feed <span>f</span></h3>
      <div class="widget-body">
        <div class="fb-cover" role="img" aria-label="Page cover showing Henrike and the blog's page name"></div>
        <p style="margin-top:8px">You and 2 other friends like this</p>
        <div class="fb-friends"><i></i><i></i><i></i><i></i><i></i><i></i></div>
      </div>
    </section>
    <section class="widget">
      <h3 class="widget-head">What our clients say</h3>
      <div class="testimonial">
        <div class="avatar" role="img" aria-label="Portrait photo of reader Marta Lindqvist"></div>
        <strong>Marta Lindqvist</strong><small>Manager</small>
        <p style="font-size:12px;margin-top:8px">Clear, friendly and honest. This blog helped our family ask better questions at the doctor.</p>
        <div class="dots"><i class="on"></i><i></i><i></i></div>
      </div>
    </section>
  </aside>
</main>

<nav class="pagination"><span class="arrow">‹</span><span>1</span><span class="on">2</span><span>3</span><span>4</span><span class="arrow">›</span></nav>

<footer class="site-footer">
  <svg class="footer-curve" width="1200" height="416" viewBox="0 0 1200 416"><path d="M0 60 Q600 -40 1200 60 V416 H0z" fill="var(--footer)"/></svg>
  <div class="footer-inner">
    <div class="socials"><i></i><i></i><i></i><i></i><i></i><i></i></div>
    <div class="footer-nav"><span>Home</span><span>Articles and links</span><span>About The Henrike</span><span>Henrike's Shop</span></div>
    <div class="footer-nav sub"><span>Contact</span><span>Reviews</span><span>Tours</span><span>FAQ</span></div>
    <div class="footer-rule"></div>
    <p class="copyright">© Copyright 2017 Lottamaus.eu, All Rights Reserved</p>
  </div>
</footer>

</body>
</html>
```